WP website design (Brenwick)

We need a wordpress design that will incorporate a professional color scheme with company logo in a clean layout. The design needs to consider that this will be developed on a responsive theme. Colors are undetermined - can use a dark red - logo is black so creative use of colors will be important. Client wants a 'modern' look.

Industry/Entity Type

It Company

Font styles to use
Serif
Sans Serif

Colors

Designer to choose colors to be used in the design.

Requirements
Must have
• Navigation: 1) Home 2) Auctions 3) Auction Services 4) Our Company 5) Contact Us

Site will have a slideshow element and the following widgets: 1) Featured Auctions 2) Testimonials blog widget 3) 'Auction Alerts' email sign up 4) Featured Videos

In the footer, there will be smaller company logo, the affiliations logo, and contact info below:
Brenwick Auction & Realty” • 3817 Marlow Creek Road •
Huntington, AR 72940 • (479) 582-3107 • tbrenwick@quelmail.com.
Nice to have
• - Site will have drop-down menus - please indicate the styling, for instance the dropdown menus 1) Upcoming Auctions 2) Past Auctions under the 'Auctions' link

```html
<!DOCTYPE html>
<html lang="en">
<head>
<meta charset="utf-8">
<title>Brenwick Auction &amp; Realty — Home</title>
<link href="https://fonts.googleapis.com/css2?family=PT+Sans:ital,wght@0,400;0,700;1,400;1,700&display=swap" rel="stylesheet">
<style>
  :root {
    --backdrop: #e6e6e6;
    --page: #ffffff;
    --ink: #2b2b2b;
    --muted: #6b6b6b;
    --teal: #1f8a80;
    --teal-light: #3aa398;
    --teal-dark: #13635c;
    --accent-line: #a8602a;
    --orange: #e8822a;
    --rule: #dcdcdc;
    --arrow-bg: #111111;
  }
  * { box-sizing: border-box; margin: 0; padding: 0; }
  html, body { width: 1200px; height: 686px; overflow: hidden; }
  body {
    background: var(--backdrop);
    font-family: "PT Sans", Arial, sans-serif;
    color: var(--ink);
    position: relative;
  }
  .site {
    position: absolute; left: 100px; top: 0;
    width: 1000px; height: 686px;
    background: var(--page);
    border-top: 4px solid var(--accent-line);
    padding: 0 20px;
  }

  /* Header */
  .site-header { position: relative; height: 84px; }
  .brand {
    position: absolute; left: 4px; top: 22px;
    display: flex; align-items: center; gap: 10px;
    font-size: 30px; font-weight: 700; color: #111; letter-spacing: .2px;
  }
  .brand-mark { width: 14px; height: 14px; background: #111; }
  .account-bar {
    position: absolute; right: 0; top: 10px;
    display: flex; align-items: center; gap: 6px; font-size: 11px;
  }
  .btn-small {
    color: #fff; padding: 2px 7px; border-radius: 2px; font-size: 10px; font-weight: 700;
  }
  .btn-login { background: var(--orange); }
  .btn-register { background: var(--teal); }
  .lang { display: flex; align-items: center; gap: 4px; margin-left: 10px; color: var(--muted); }
  .lang-swatch { width: 14px; height: 9px; background: #3a4f8c; }
  .tools-bar {
    position: absolute; right: 0; top: 44px;
    display: flex; align-items: center; gap: 5px;
  }
  .social-dot { width: 16px; height: 16px; border-radius: 50%; border: 1.5px solid var(--teal-light); }
  .social-dot.feed { border-color: var(--orange); }
  .search-box {
    margin-left: 14px; width: 86px; height: 18px;
    border: 1px solid #9fd07a; border-radius: 2px; position: relative;
  }
  .search-box svg { position: absolute; right: 4px; top: 3px; }

  /* Navigation */
  .main-nav {
    position: relative; height: 32px; border-radius: 3px;
    background: linear-gradient(90deg, var(--teal-dark), var(--teal) 50%, var(--teal-light));
    display: flex; justify-content: center;
  }
  .main-nav a {
    color: #fff; text-decoration: none; font-size: 13px; font-weight: 700;
    line-height: 32px; padding: 0 14px; position: relative;
  }
  .main-nav a + a::before {
    content: ""; position: absolute; left: 0; top: 9px; height: 14px; border-left: 1px solid rgba(255,255,255,.35);
  }
  .main-nav .is-active { background: rgba(0,0,0,.18); }
  .dropdown {
    position: absolute; top: 32px; left: 0; width: 118px; z-index: 5;
    background: var(--teal-dark); border-top: 2px solid #0b3d39;
  }
  .dropdown span {
    display: block; color: #fff; font-size: 11px; font-weight: 700; padding: 4px 10px;
  }
  .dropdown span + span { border-top: 1px solid rgba(255,255,255,.15); }

  /* Slideshow */
  .slideshow {
    position: relative; margin-top: 8px; height: 252px;
    background: linear-gradient(180deg, #8fbbe0 0%, #c4dcec 30%, #e8ded0 55%, #cdbba5 75%, #6e8f4a 100%);
  }
  .slide-arrow {
    position: absolute; top: 108px; width: 20px; height: 30px; background: var(--arrow-bg);
    display: flex; align-items: center; justify-content: center;
  }
  .slide-arrow.prev { left: 0; }
  .slide-arrow.next { right: 0; }
  .slide-dots { position: absolute; bottom: 10px; left: 50%; transform: translateX(-50%); display: flex; gap: 6px; }
  .slide-dots i { width: 8px; height: 8px; border-radius: 50%; background: rgba(255,255,255,.7); }
  .slide-dots i.on { background: var(--teal); }

  /* Content */
  .content { display: flex; gap: 30px; margin-top: 16px; }
  .intro { width: 610px; }
  .intro h1 { font-size: 20px; font-weight: 400; }
  .intro h1 em { color: var(--teal); font-weight: 700; }
  .intro p { font-size: 12.5px; line-height: 1.5; color: var(--muted); margin-top: 6px; }
  .listing {
    display: flex; gap: 14px; margin-top: 12px; padding-top: 10px; border-top: 1px solid var(--rule);
  }
  .listing-photo { width: 104px; height: 62px; background: linear-gradient(180deg, #9cc3e0, #e3d6c4 55%, #7a9a57); }
  .listing h3 { font-size: 13px; color: var(--ink); }
  .listing .meta { font-size: 11.5px; color: var(--muted); margin: 2px 0 6px; }
  .btn-details {
    display: inline-block; background: var(--teal); color: #fff; font-size: 10.5px; font-weight: 700;
    padding: 2px 10px; border-radius: 2px;
  }

  .sidebar { width: 320px; }
  .widget-title {
    position: relative; height: 26px; background: var(--teal); color: #fff;
    font-size: 12px; font-weight: 700; line-height: 26px; padding-left: 10px; width: 190px;
  }
  .widget-title::after {
    content: ""; position: absolute; right: -13px; top: 0;
    border-left: 13px solid var(--teal); border-top: 13px solid transparent; border-bottom: 13px solid transparent;
  }
  .widget-head { display: flex; justify-content: space-between; align-items: center; }
  .pager { display: flex; gap: 2px; }
  .pager i { width: 14px; height: 12px; background: #555; }
  .featured-photo { margin-top: 8px; height: 104px; background: linear-gradient(180deg, #a6c9e4, #ece2d4 55%, #7f9d5b); }
  .featured-caption { font-size: 12px; font-weight: 700; color: var(--teal); margin-top: 4px; }
  .alerts {
    margin-top: 10px; background: var(--teal); color: #fff; padding: 9px 10px 10px;
  }
  .alerts h4 { font-size: 13px; }
  .alerts p { font-size: 11px; margin: 2px 0 6px; }
  .alerts-form { display: flex; gap: 4px; }
  .alerts-input { flex: 1; height: 20px; background: #fff; color: #999; font-size: 10.5px; padding: 3px 6px; }
  .alerts-button { background: var(--teal-dark); font-size: 10.5px; font-weight: 700; padding: 3px 10px; }
</style>
</head>
<body>
  <div class="site">
    <header class="site-header">
      <div class="brand"><span class="brand-mark"></span>Brenwick Auction &amp; Realty</div>
      <div class="account-bar">
        <span class="btn-small btn-login">Log In</span>
        <span class="btn-small btn-register">Register</span>
        <span class="lang"><span class="lang-swatch"></span>Eng ▾</span>
      </div>
      <div class="tools-bar">
        <span class="social-dot"></span>
        <span class="social-dot"></span>
        <span class="social-dot"></span>
        <span class="social-dot feed"></span>
        <span class="search-box">
          <svg width="11" height="11" viewBox="0 0 11 11"><circle cx="4.5" cy="4.5" r="3.3" fill="none" stroke="#8cc46a" stroke-width="1.4"/><line x1="7" y1="7" x2="10" y2="10" stroke="#8cc46a" stroke-width="1.6"/></svg>
        </span>
      </div>
    </header>

    <nav class="main-nav">
      <a>Home</a>
      <a class="is-active">Auctions
        <span class="dropdown"><span>Upcoming Auctions</span><span>Past Auctions</span></span>
      </a>
      <a>Auction Services</a>
      <a>Our Company</a>
      <a>Contact Us</a>
    </nav>

    <section class="slideshow" role="img" aria-label="Slideshow photo of a two-storey cream house with bay windows under a blue sky">
      <span class="slide-arrow prev"><svg width="8" height="12" viewBox="0 0 8 12"><path d="M6 1 1 6l5 5" fill="none" stroke="#fff" stroke-width="2"/></svg></span>
      <span class="slide-arrow next"><svg width="8" height="12" viewBox="0 0 8 12"><path d="M2 1l5 5-5 5" fill="none" stroke="#fff" stroke-width="2"/></svg></span>
      <div class="slide-dots"><i></i><i class="on"></i><i></i><i></i></div>
    </section>

    <div class="content">
      <main class="intro">
        <h1>Welcome to <em>Brenwick Auction &amp; Realty</em></h1>
        <p>Three decades of honest, well-run auctions for homes, farmland and estates across western Arkansas. Browse upcoming sales below or call our team to list your property.</p>
        <article class="listing">
          <div class="listing-photo" role="img" aria-label="Photo of a brick family home"></div>
          <div>
            <h3>Brick family home on two acres</h3>
            <div class="meta">Sat, June 14 · 10:00 AM</div>
            <span class="btn-details">View Details</span>
          </div>
        </article>
        <article class="listing">
          <div class="listing-photo" role="img" aria-label="Photo of a country cottage by a pond"></div>
          <div>
            <h3>Country cottage with pond</h3>
            <div class="meta">Sat, June 21 · 11:00 AM</div>
            <span class="btn-details">View Details</span>
          </div>
        </article>
      </main>

      <aside class="sidebar">
        <div class="widget-head">
          <div class="widget-title">FEATURED AUCTIONS</div>
          <div class="pager"><i></i><i></i></div>
        </div>
        <div class="featured-photo" role="img" aria-label="Photo of a featured lakeside ranch house"></div>
        <div class="featured-caption">Lakeside ranch, Huntington AR</div>
        <div class="alerts">
          <h4>Auction Alerts</h4>
          <p>Get new sales by email</p>
          <div class="alerts-form">
            <span class="alerts-input">Your email</span>
            <span class="alerts-button">Sign Up</span>
          </div>
        </div>
      </aside>
    </div>
  </div>
</body>
</html>
```